Executive Taxi firm with Chauffeur service Website

I have my domain name registered and I have started to work on my site but I am struggling. I am just about to get a logo for the company and need a web site that clearly represents the fact we are an executive/luxury brand in private hire vehicles. We offer airport transfers, train station transfers, seaport transfers, holiday transfers and business to business pick up and drop off.

Target Market(s)

Corporate people, holidaymakers looking for a luxury start their holiday. VIPs' and celebrities.

Number of Pages Required

5+ page

Font styles to use
Serif
Sans Serif
Decorative
Script

Colors

Designer to choose colors to be used in the design.

Requirements
Must have
• Home Page, Services, About Us, VIP and Contact us
• Please see www.brookvane.co.uk I have started it but not happy with it at all.
Nice to have
• Booking form or enquiry form.

```html
<!DOCTYPE html>
<html lang="en">
<head>
<meta charset="utf-8">
<title>Brookvane – Executive Private Hire</title>
<link rel="stylesheet" href="https://fonts.googleapis.com/css2?family=Open+Sans:ital,wght@0,400;0,600;0,700;0,800;1,400;1,600&display=swap">
<style>
:root{
  --red:#e0262d;
  --gold:#f6b40e;
  --ink:#222;
  --text:#555;
  --muted:#888;
  --line:#ddd;
  --bg-soft:#f1f1f1;
  --white:#fff;
}
*{box-sizing:border-box;margin:0;padding:0}
html,body{width:1200px;height:2936px;overflow:hidden}
body{font-family:"Open Sans",Arial,sans-serif;color:var(--text);background:var(--white);font-size:12px;position:relative}
.wrap{width:880px;margin:0 auto;position:relative}
a{color:inherit;text-decoration:none}

/* top bar */
.topbar{height:40px;background:#f4f4f4;border-bottom:1px solid #e6e6e6}
.topbar .wrap{display:flex;justify-content:space-between;align-items:center;height:40px}
.social{display:flex;gap:18px}
.social span{width:11px;height:11px;border-radius:50%;background:#8a8a8a;display:block}
.account{font-size:11px;color:#666}
.account b{font-weight:400;margin:0 8px;color:#aaa}

/* header */
.header{height:93px;background:var(--white)}
.header .wrap{display:flex;align-items:center;height:93px}
.brand{display:flex;align-items:center;gap:10px;font-size:34px;font-weight:700;color:#555;letter-spacing:.5px}
.brand i{width:30px;height:30px;border-radius:50%;background:var(--red);display:block}
.contacts{margin-left:auto;display:flex;gap:60px}
.contact{display:flex;align-items:center;gap:14px}
.contact small{display:block;font-size:11px;color:#666;text-transform:uppercase}
.contact strong{display:block;font-size:16px;font-weight:400;color:#444}
.contact strong.hot{color:var(--red);font-weight:600}

/* nav */
.nav{height:49px;border-top:1px solid #e3e3e3;border-bottom:1px solid #e3e3e3}
.nav .wrap{display:flex;height:47px;align-items:stretch}
.nav a{font-size:11px;font-weight:600;color:#333;display:flex;align-items:center;padding:0 18px;text-transform:uppercase;margin-right:22px}
.nav a.active{border-bottom:3px solid var(--red)}
.nav a.book{margin-left:auto;margin-right:0;background:var(--red);color:var(--white);padding:0 32px}

/* hero */
.hero{height:429px;position:relative;background:linear-gradient(180deg,#2a2f38 0%,#4a4f58 45%,#3a3d44 100%)}
.hero .wrap{height:429px}
.booking{position:absolute;left:2px;top:63px;width:275px;height:309px;background:var(--white);padding:22px 22px}
.tabs{display:flex;justify-content:center;gap:8px;font-size:9px;font-weight:700;color:#333}
.tabs span{padding:4px 10px;border-radius:10px}
.tabs .on{background:var(--red);color:var(--white)}
.booking h4{text-align:center;font-size:9px;font-weight:700;color:#333;margin:8px 0 14px}
.field-row{display:flex;gap:14px;margin-bottom:16px}
.field{flex:1;border-bottom:1px solid #ccc;font-size:9px;color:#999;padding-bottom:7px}
.submit{background:#1e1e1e;color:var(--white);text-align:center;font-size:10px;font-weight:700;padding:9px 0;margin-top:10px}
.hero-copy{position:absolute;left:352px;top:120px}
.hero-copy h1{font-size:37px;font-weight:800;color:var(--gold);line-height:46px;text-transform:uppercase}
.hero-copy h2{font-size:29px;font-weight:700;color:var(--white);margin-top:6px;text-transform:uppercase}
.btn{display:inline-block;background:var(--red);color:var(--white);font-size:12px;text-transform:uppercase;padding:9px 20px}
.hero-copy .btn{margin-top:26px}
.slider-dots{position:absolute;right:164px;bottom:22px;display:flex;gap:7px}
.slider-dots span{width:7px;height:7px;background:var(--white)}
.slider-dots .on{background:var(--red)}

/* cars */
.cars{height:426px;background:var(--bg-soft);padding-top:42px}
.sec-head{display:flex;justify-content:space-between;align-items:center}
.sec-head h3{font-size:18px;font-weight:700;color:#222;border-left:3px solid var(--red);padding-left:10px;text-transform:uppercase}
.arrows{display:flex;gap:4px}
.arrows span{width:22px;height:22px;background:#555;display:flex;align-items:center;justify-content:center}
.car-grid{display:flex;gap:21px;margin-top:25px}
.car{width:204px;height:300px;background:var(--white);padding:14px 20px;box-shadow:0 1px 3px rgba(0,0,0,.08)}
.car .photo{height:100px;background:radial-gradient(ellipse at center,#6c6c70 0%,#c9c9cc 55%,#fff 75%)}
.car h5{font-size:10px;font-weight:700;color:#222;margin-top:22px;text-transform:uppercase}
.car h5::after{content:"";display:block;width:22px;height:2px;background:var(--red);margin-top:6px}
.car p{font-size:10px;color:#444;margin-top:8px;line-height:14px}
.car ul{list-style:none;margin-top:10px}
.car li{font-size:10px;color:#555;display:flex;align-items:center;gap:8px;margin-bottom:8px}
.car li i{width:8px;height:8px;border-radius:50%;border:1px solid #888;display:block}
.car .btn{font-size:9px;padding:6px 14px;font-weight:600}

/* always here */
.always{height:470px;padding-top:40px;position:relative}
.always .wrap{height:430px}
.title{text-align:center;font-size:17px;font-weight:700;color:#222;text-transform:uppercase}
.title::after{content:"";display:block;width:70px;border-bottom:2px dotted #333;margin:14px auto 0}
.always .lead{width:600px;margin:24px auto 0;text-align:center;font-size:11px;line-height:17px;color:#444}
.feature{position:absolute;width:230px}
.feature h6{font-size:13px;font-weight:700;color:#222;text-transform:uppercase}
.feature p{font-size:11px;line-height:16px;color:#555;margin-top:8px}
.feature svg{position:absolute;top:0}
.feature.left{left:0;padding-left:50px}
.feature.left svg{left:0}
.feature.right{right:0;text-align:right;padding-right:50px}
.feature.right svg{right:0}
.feature.row1{top:176px}
.feature.row2{top:288px}
.hero-car{position:absolute;left:251px;top:165px;width:372px;height:205px;background:radial-gradient(ellipse at center,#9a9ca0 0%,#d4d5d8 50%,#fff 72%)}
.always .btn{position:absolute;left:394px;top:392px;font-size:9px;padding:7px 18px;font-weight:600}

/* offers */
.offers{height:760px;padding-top:26px}
.offer-grid{display:grid;grid-template-columns:repeat(3,278px);gap:25px 22px;margin-top:30px}
.offer{height:293px;border:1px solid #ccc;background:var(--white)}
.offer .photo{height:188px}
.offer h5{font-size:10px;font-weight:700;color:#222;margin:20px 14px 0;text-transform:uppercase}
.offer p{font-size:10px;line-height:14px;color:#444;margin:6px 14px 0}
.offer .more{display:block;text-align:right;font-size:9px;font-weight:700;color:var(--red);margin:14px 14px 0}
.offers .btn{display:block;width:90px;margin:32px auto 0;font-size:9px;padding:7px 0;text-align:center;font-weight:600}

/* testimonials */
.testimonials{height:300px;background:linear-gradient(180deg,#e7e7e7,#dcdcdc 50%,#ebebeb);padding-top:86px;text-align:center}
.testimonials blockquote{width:620px;margin:28px auto 0;font-style:italic;font-weight:600;font-size:14px;line-height:20px;color:#777}
.testimonials blockquote b{color:var(--gold);font-style:normal}
.testimonials cite{display:block;margin-top:12px;font-style:normal;font-size:14px;color:#333}
.tdots{display:flex;justify-content:center;gap:7px;margin-top:16px}
.tdots span{width:7px;height:7px;background:#444}
.tdots .on{background:var(--red)}

/* footer */
.footer{height:369px;padding-top:44px;overflow:hidden}
.foot-cols{display:flex}
.foot-about{width:300px}
.foot-about .brand{font-size:28px}
.foot-about .brand i{width:26px;height:26px}
.foot-about p{font-size:10px;line-height:16px;color:#555;margin-top:12px;width:280px}
.foot-col{width:151px}
.foot-col h6{font-size:13px;font-weight:700;color:#222;text-transform:uppercase;margin-top:2px}
.foot-col li{list-style:none;font-size:10px;color:#555;margin-top:13px}
.foot-get{flex:1}
.foot-get h6{font-size:13px;font-weight:700;color:#222;text-transform:uppercase;margin-top:2px}
.foot-get .addr{font-size:10px;line-height:15px;color:#555;margin-top:14px}
.foot-get .addr b{color:var(--red);font-weight:400}
.foot-get .line{display:flex;align-items:center;gap:10px;margin-top:12px;font-size:15px;color:#444}
.foot-get .line.hot{color:var(--red);font-weight:600}
.foot-social{display:flex;gap:24px;margin:16px 0 0 12px}
.foot-social span{width:11px;height:11px;border-radius:50%;background:var(--red);display:block}
.payments{display:flex;justify-content:center;gap:12px;margin-top:28px;padding-top:20px;border-top:1px solid #e5e5e5}
.payments span{width:60px;height:26px;background:#e9e9ee;border-radius:3px;display:block}
.payments span:nth-child(odd){background:#dfe3ea}
.copy{text-align:center;font-size:9px;color:#777;margin-top:28px}
</style>
</head>
<body>

<div class="topbar"><div class="wrap">
  <div class="social"><span></span><span></span><span></span><span></span></div>
  <div class="account">Login<b>|</b>Sign Up</div>
</div></div>

<header class="header"><div class="wrap">
  <div class="brand"><i></i>BROOKVANE</div>
  <div class="contacts">
    <div class="contact">
      <svg width="44" height="26" viewBox="0 0 44 26"><g stroke="#444" stroke-width="1.6" fill="none"><rect x="14" y="3" width="28" height="20"/><path d="M14 3l14 11 14-11"/><path d="M0 8h10M3 13h8M0 18h10"/></g></svg>
      <div><small>Email us</small><strong>info@brookvane.co.uk</strong></div>
    </div>
    <div class="contact">
      <svg width="26" height="26" viewBox="0 0 26 26"><path d="M6 2l5 5-3 3c1.5 3.5 4.5 6.5 8 8l3-3 5 5-3.5 3.5C12 22 4 14 2.5 5.5z" fill="none" stroke="#444" stroke-width="1.6"/></svg>
      <div><small>Call us any time:</small><strong class="hot">07000 418263</strong></div>
    </div>
  </div>
</div></header>

<nav class="nav"><div class="wrap">
  <a class="active" href="#">Home</a>
  <a href="#">Services</a>
  <a href="#">About Us</a>
  <a href="#">VIP</a>
  <a href="#">Contact Us</a>
  <a class="book" href="#">Book for a ride</a>
</div></nav>

<section class="hero" role="img" aria-label="Dusk photograph of a city bridge with towers behind the booking panel">
  <div class="wrap">
    <form class="booking">
      <div class="tabs"><span class="on">ONEWAY</span><span>ROUNDTRIP</span><span>PACKAGES</span></div>
      <h4>ESTIMATED BOOK NOW</h4>
      <div class="field-row"><div class="field">Your Name</div></div>
      <div class="field-row"><div class="field">Phone Number</div><div class="field">Passengers</div></div>
      <div class="field-row"><div class="field">Pick Up Date</div><div class="field">Pick Up Time</div></div>
      <div class="field-row"><div class="field">Travel From</div><div class="field">Travel To</div></div>
      <div class="submit">Submit</div>
    </form>
    <div class="hero-copy">
      <h1>Private Hire,Chauffeur<br>&amp; Taxi Service</h1>
      <h2>Executive Brookvane Travel</h2>
      <a class="btn" href="#">Book Now</a>
    </div>
  </div>
  <div class="slider-dots"><span class="on"></span><span></span><span></span></div>
</section>

<section class="cars"><div class="wrap">
  <div class="sec-head">
    <h3>Available Cars</h3>
    <div class="arrows">
      <span><svg width="8" height="8" viewBox="0 0 8 8"><path d="M5 1L2 4l3 3" stroke="#fff" fill="none" stroke-width="1.5"/></svg></span>
      <span><svg width="8" height="8" viewBox="0 0 8 8"><path d="M3 1l3 3-3 3" stroke="#fff" fill="none" stroke-width="1.5"/></svg></span>
    </div>
  </div>
  <div class="car-grid">
    <article class="car">
      <div class="photo" role="img" aria-label="Black executive saloon car"></div>
      <h5>Brookvane Taxi</h5>
      <p>Cars we offer for 4+1 Seater<br>CITY COMPACT</p>
      <ul><li><i></i>4+1 Seater</li><li><i></i>₹8/km</li><li><i></i>A/c</li></ul>
      <a class="btn" href="#">Cab Booking</a>
    </article>
    <article class="car">
      <div class="photo" role="img" aria-label="Silver saloon car"></div>
      <h5>Brookvane Taxi</h5>
      <p>Cars we offer for 4+1 Seater<br>SALOON PLUS</p>
      <ul><li><i></i>4+1 Seater</li><li><i></i>₹8/km</li><li><i></i>A/c</li></ul>
      <a class="btn" href="#">Cab Booking</a>
    </article>
    <article class="car">
      <div class="photo" role="img" aria-label="Black people carrier van"></div>
      <h5>Brookvane Taxi</h5>
      <p>Cars we offer for 7+1 Seater<br>EXEC SEVEN</p>
      <ul><li><i></i>7+1 Seater</li><li><i></i>₹8/km</li><li><i></i>A/c</li></ul>
      <a class="btn" href="#">Cab Booking</a>
    </article>
    <article class="car">
      <div class="photo" role="img" aria-label="Silver minibus"></div>
      <h5>Brookvane Taxi</h5>
      <p>Cars we offer for 9+1 Seater<br>GROUP NINE</p>
      <ul><li><i></i>9+1 Seater</li><li><i></i>₹8/km</li><li><i></i>A/c</li></ul>
      <a class="btn" href="#">Cab Booking</a>
    </article>
  </div>
</div></section>

<section class="always"><div class="wrap">
  <h3 class="title">Always Here For You</h3>
  <p class="lead">We provide airport transfers to and from all major UK airports, seaports, train station transfers and an executive business to business transfer service. Whether you have an individual or group transfer request, our company-owned fleet offers a choice of options to suit your needs, from luxury saloons and SUV's to 9-seat luxury transporters.</p>

  <div class="feature left row1">
    <svg width="34" height="34" viewBox="0 0 34 34"><circle cx="17" cy="17" r="14" fill="none" stroke="#e0262d" stroke-width="2"/><text x="17" y="21" font-size="10" font-weight="700" fill="#e0262d" text-anchor="middle" font-family="Open Sans, sans-serif">24</text></svg>
    <h6>24X7 Service</h6>
    <p>Vitae leo dictum, sodales lorem vitae, sollicitudin dui.</p>
  </div>
  <div class="feature left row2">
    <svg width="34" height="34" viewBox="0 0 34 34"><g fill="none" stroke="#e0262d" stroke-width="2"><circle cx="17" cy="9" r="5"/><path d="M7 32V22c0-4 4-7 10-7s10 3 10 7v10z"/></g></svg>
    <h6>Corporate Service</h6>
    <p>Vitae leo dictum, sodales lorem vitae, sollicitudin dui.</p>
  </div>
  <div class="feature right row1">
    <svg width="34" height="34" viewBox="0 0 34 34"><g fill="none" stroke="#e0262d" stroke-width="2"><path d="M17 30s-9-9-9-16a9 9 0 0118 0c0 7-9 16-9 16z"/><circle cx="17" cy="14" r="3"/></g></svg>
    <h6>GPS Tracking</h6>
    <p>Vitae leo dictum, sodales lorem vitae, sollicitudin dui.</p>
  </div>
  <div class="feature right row2">
    <svg width="34" height="34" viewBox="0 0 34 34"><g fill="none" stroke="#e0262d" stroke-width="2"><path d="M4 22l4-10h18l4 10v6H4z"/><circle cx="10" cy="28" r="3"/><circle cx="24" cy="28" r="3"/></g></svg>
    <h6>Tour Package</h6>
    <p>Vitae leo dictum, sodales lorem vitae, sollicitudin dui.</p>
  </div>

  <div class="hero-car" role="img" aria-label="Silver executive saloon car, front three-quarter view"></div>
  <a class="btn" href="#">Book Now</a>
</div></section>

<section class="offers"><div class="wrap">
  <h3 class="title">We Offers</h3>
  <div class="offer-grid">
    <article class="offer">
      <div class="photo" role="img" aria-label="Private jet on the runway beside a chauffeur car" style="background:linear-gradient(180deg,#9cc3e6,#d8e4ee 55%,#8d9096)"></div>
      <h5>Airport Transfers</h5>
      <p>Nullam orci dui, dictum et magna sollicitudin, tempor blandit erat.</p>
      <a class="more" href="#">READ MORE ...</a>
    </article>
    <article class="offer">
      <div class="photo" role="img" aria-label="Black executive car in front of a train at a station" style="background:linear-gradient(180deg,#bfa66a,#4a4a4c 55%,#2a2a2c)"></div>
      <h5>Train Station Transfers</h5>
      <p>Nullam orci dui, dictum et magna sollicitudin, tempor blandit erat.</p>
      <a class="more" href="#">READ MORE ...</a>
    </article>
    <article class="offer">
      <div class="photo" role="img" aria-label="Executive car parked at a seaport with a cruise ship behind" style="background:linear-gradient(180deg,#8db4dc,#c9d4de 45%,#3c3e42)"></div>
      <h5>Seaport Transfers</h5>
      <p>Nullam orci dui, dictum et magna sollicitudin, tempor blandit erat.</p>
      <a class="more" href="#">READ MORE ...</a>
    </article>
    <article class="offer">
      <div class="photo" role="img" aria-label="White SUV driving along a tree-lined road" style="background:linear-gradient(180deg,#5f8a3a,#9bb36a 50%,#7c7a72)"></div>
      <h5>Holiday Transfers</h5>
      <p>Nullam orci dui, dictum et magna sollicitudin, tempor blandit erat.</p>
      <a class="more" href="#">READ MORE ...</a>
    </article>
    <article class="offer">
      <div class="photo" role="img" aria-label="Businessman on the phone beside a taxi in the city" style="background:linear-gradient(180deg,#c9b070,#6b6f78 55%,#3a3d44)"></div>
      <h5>Business To Business Transfers</h5>
      <p>Nullam orci dui, dictum et magna sollicitudin, tempor blandit erat.</p>
      <a class="more" href="#">READ MORE ...</a>
    </article>
    <article class="offer">
      <div class="photo" role="img" aria-label="Chauffeur holding open the rear door of a black car" style="background:linear-gradient(180deg,#1c1c1e,#4a4440 55%,#c7b28e)"></div>
      <h5>Pick Up And Drop Off</h5>
      <p>Nullam orci dui, dictum et magna sollicitudin, tempor blandit erat.</p>
      <a class="more" href="#">READ MORE ...</a>
    </article>
  </div>
  <a class="btn" href="#">View More</a>
</div></section>

<section class="testimonials">
  <h3 class="title">What Our Coustmer Say</h3>
  <blockquote><b>“</b> Lorem ipsum dolor sit amet, consectetur adipiscing elit. Nunc facilisis lacus a nisi congue, sed porta elit efficitur. Morbi suscipit arcu et rutrum faucibus. Curabitur tristique eros tellus, quis laoreet nisl viverra nec. Aenean auctor lorem nec cursus aliquet. <b>”</b></blockquote>
  <cite>- Fusce ornare</cite>
  <div class="tdots"><span class="on"></span><span></span><span></span></div>
</section>

<footer class="footer"><div class="wrap">
  <div class="foot-cols">
    <div class="foot-about">
      <div class="brand"><i></i>BROOKVANE</div>
      <p>We provide a door-to-door convenience from your home, office or hotel straight to any destination of your choice. Pre-booked or last minute we aim to cover any transport requirement. Airports and train station service: All pick-ups from arrivals will of been briefed as to your exact pickup point, or your chauffeur will be waiting with a name board.</p>
    </div>
    <div class="foot-col">
      <h6>Quick Links</h6>
      <ul><li>Home</li><li>Services</li><li>About Us</li><li>VIP</li><li>Contact Us</li></ul>
    </div>
    <div class="foot-col">
      <h6>Services</h6>
      <ul><li>Local Car Rentals</li><li>Outstation Taxi</li><li>One way cabs</li><li>Cabs by City</li><li>Allport Transfers</li></ul>
    </div>
    <div class="foot-get">
      <h6>Get In Touch</h6>
      <p class="addr"><b>Address:</b> 21 Proin facilisis ornare est non placerat<br>Donec sagittis orci non felis</p>
      <div class="line hot"><svg width="16" height="16" viewBox="0 0 26 26"><path d="M6 2l5 5-3 3c1.5 3.5 4.5 6.5 8 8l3-3 5 5-3.5 3.5C12 22 4 14 2.5 5.5z" fill="none" stroke="#444" stroke-width="2"/></svg>07000 418263</div>
      <div class="line"><svg width="18" height="14" viewBox="0 0 18 14"><g fill="none" stroke="#444" stroke-width="1.4"><rect x="1" y="1" width="16" height="12"/><path d="M1 1l8 7 8-7"/></g></svg>info@brookvane.co.uk</div>
      <div class="foot-social"><span></span><span></span></div>
    </div>
  </div>
  <div class="payments"><span></span><span></span><span></span><span></span><span></span><span></span><span></span><span></span><span></span><span></span><span></span></div>
  <p class="copy">Copyright © 2018 Brookvane. All Rights Reserved.</p>
</div></footer>

</body>
</html>
```